Larkwood Bend Campground Billboard

We need an eye-catching, traffic-stopping design for a 15 ft x 10 ft billboard that will be located near the turn-off to our RV park in Colorado. Our park is located on the banks of the Rio Grande River and we want to emphasize that we have shady spots on the river. This is a link to our website www.larkwoodbendcampground.com and it will give you an idea about our park and what we have to offer. The billboard will be double-sided and face both directions of a busy highway. The park and the river is not visible from the highway, so we want to attract attention.

Target Market(s)

RV travelers on US Hwy 160 in South Fork, Colorado

Font styles to use
Sans Serif

Colors

Designer to choose colors to be used in the design.

Requirements
Must have
• Simple, eye-catching message.
Nice to have
• Incorporate our logo and give directions.
Should not have
• Too much information that can't be read while speeding down a busy highway.

```html
<!DOCTYPE html>
<html lang="en">
<head>
<meta charset="utf-8">
<title>Larkwood Bend Campground Billboard</title>
<link href="https://fonts.googleapis.com/css2?family=Bree+Serif&family=Michroma&family=Oswald:wght@400;500&family=Roboto+Condensed:wght@700&display=swap" rel="stylesheet">
<style>
  :root{
    --ink:#262a44;
    --ribbon:#1aa3e0;
    --ribbon-dark:#1b3f7a;
    --white:#ffffff;
    --yellow:#f5e81c;
    --pink:#e6268e;
    --orange:#f28a2e;
    --red:#e8383b;
    --blue:#1c9ad8;
    --brand:#1f3a22;
  }
  *{margin:0;padding:0;box-sizing:border-box}
  html,body{width:1200px;height:800px;overflow:hidden}
  .billboard{position:relative;width:1200px;height:800px;overflow:hidden;font-family:"Oswald",sans-serif}
  .scenery{position:absolute;inset:0;
    background:linear-gradient(180deg,#7fb4dc 0%,#c7dcea 18%,#e6eef2 40%,#dbe8e6 50%,#4f9a3a 56%,#2f8a2a 64%,#3e9a34 70%,#6aa85a 76%,#a9c3c4 84%,#c9d9e0 100%)}
  .contact-ribbon{position:absolute;left:0;top:68px;width:734px;height:70px}
  .contact-ribbon svg{position:absolute;inset:0}
  .website{position:absolute;left:50px;top:18px;font-family:"Roboto Condensed",sans-serif;font-weight:700;font-size:24px;color:var(--white);letter-spacing:0.2px;white-space:nowrap}
  .divider{position:absolute;left:436px;top:19px;width:2px;height:32px;background:rgba(255,255,255,.8)}
  .phone{position:absolute;left:458px;top:5px;font-family:"Oswald",sans-serif;font-weight:500;font-size:42px;line-height:1.2;color:var(--white);white-space:nowrap}
  .brand-name{position:absolute;right:34px;top:58px;width:230px;text-align:center;font-family:"Oswald",sans-serif;font-weight:500;font-size:30px;line-height:1.05;color:var(--brand);text-transform:uppercase}
  .headline{position:absolute;left:0;top:192px;width:1200px;text-align:center;font-family:"Bree Serif",serif;font-weight:400;font-size:120px;line-height:108px;color:var(--ink);white-space:nowrap}
  .offers-title{position:absolute;left:0;top:570px;width:1200px;text-align:center;font-family:"Michroma",sans-serif;font-weight:400;font-size:30px;letter-spacing:1px;color:var(--white);white-space:nowrap}
  .tag{position:absolute;height:64px;display:flex;align-items:center;justify-content:center;font-family:"Oswald",sans-serif;font-weight:400;font-size:31px;line-height:1;letter-spacing:-0.3px;white-space:nowrap;color:var(--white);text-transform:uppercase;box-shadow:4px 4px 6px rgba(0,0,0,.35);overflow:hidden}
  .tag-rv{left:54px;top:628px;width:244px;background:var(--yellow);color:var(--ink)}
  .tag-river{left:310px;top:628px;width:280px;background:var(--pink)}
  .tag-tent{left:602px;top:628px;width:169px;background:var(--orange)}
  .tag-fishing{left:784px;top:628px;width:362px;background:var(--red)}
  .tag-amenities{left:235px;top:706px;width:730px;background:var(--blue)}
</style>
</head>
<body>
<main class="billboard">
  <div class="scenery" role="img" aria-label="Photo of a calm river lined with green trees beneath a forested hillside and a soft blue sky"></div>

  <div class="contact-ribbon">
    <svg width="734" height="70" viewBox="0 0 734 70">
      <polygon points="0,0 734,0 708,35 734,70 0,70" fill="var(--ribbon)"/>
      <rect x="0" y="0" width="24" height="70" fill="var(--ribbon-dark)"/>
    </svg>
    <span class="website">www.larkwoodbendcampground.com</span>
    <span class="divider"></span>
    <span class="phone">800 555 0147</span>
  </div>

  <div class="brand-name">Larkwood Bend<br>Campground</div>

  <h1 class="headline">Make your visit<br>an enjoyable one</h1>

  <h2 class="offers-title">CAMPGROUND OFFERS</h2>

  <div class="tag tag-rv">Large RV Spaces</div>
  <div class="tag tag-river">Riverfront Spaces</div>
  <div class="tag tag-tent">Tent Sites</div>
  <div class="tag tag-fishing">Fishing on the Rio Grande</div>
  <div class="tag tag-amenities">Access to our large array of campground amenities</div>
</main>
</body>
</html>
```